Web Developer Needs a Business Card Design

I need a personal business card design that represents me as a web developer for potential employers. I would like the background to be a dark color on the front for contrast with my logo and name. The back will have all my information along with a smaller version of the logo. I want something with a modern look and feel, not too conservative. This will be used for potential employers and freelance work.

Industry/Entity Type

Business

Contact Information for Business Card

Front should have my logo and name. The back should have all my personal information which would include: name: Tom Brevardi, phone: 570-614-9083, email: tombrevardi@mailwisp.com, website url: www.tombrevardi.com, logo, web developer.

Font styles to use
Sans Serif

Requirements
Must have
• Must include my logo. The color palette base color will be the logo color.

```html
<!DOCTYPE html>
<html lang="en">
<head>
<meta charset="utf-8">
<title>Tom Brevardi – Business Card</title>
<link href="https://fonts.googleapis.com/css2?family=Lato:wght@400;700&display=swap" rel="stylesheet">
<style>
  :root {
    --backdrop: #1a1a1a;
    --card-white: #ffffff;
    --brand-teal: #46b79a;
    --brand-teal-deep: #258c73;
    --ink: #222222;
    --on-teal: #ffffff;
  }
  html, body {
    margin: 0;
    padding: 0;
    width: 1200px;
    height: 1086px;
    overflow: hidden;
    background: var(--backdrop);
    font-family: "Lato", sans-serif;
  }
  .canvas {
    position: relative;
    width: 1200px;
    height: 1086px;
  }
  .card {
    position: absolute;
    left: 254px;
    width: 677px;
    height: 387px;
    border-radius: 8px;
  }
  .card--front { top: 126px; background: var(--card-white); }
  .card--back  { top: 586px; background: var(--brand-teal-deep); }

  .brand-ring {
    position: absolute;
    box-sizing: border-box;
    border-radius: 50%;
  }
  .card--front .brand-ring {
    left: 132px; top: 111px;
    width: 128px; height: 128px;
    border: 10px solid var(--brand-teal);
  }
  .wordmark {
    position: absolute;
    left: 66px; top: 246px;
    width: 260px;
    text-align: center;
    font-weight: 700;
    font-size: 33px;
    line-height: 40px;
    letter-spacing: -0.3px;
    color: var(--brand-teal);
    white-space: nowrap;
  }
  .divider {
    position: absolute;
    left: 338px; top: 112px;
    width: 2px; height: 172px;
    background: linear-gradient(var(--brand-teal) 0 36%, var(--ink) 36% 100%);
  }
  .identity {
    position: absolute;
    left: 366px; top: 110px;
  }
  .identity__name {
    margin: 0;
    font-weight: 700;
    font-size: 27px;
    line-height: 34px;
    color: var(--brand-teal);
  }
  .identity__title {
    margin: 0;
    font-size: 21px;
    line-height: 26px;
    color: var(--ink);
  }
  .contact-list {
    position: absolute;
    left: 364px; top: 197px;
    margin: 0; padding: 0;
    list-style: none;
  }
  .contact-list li {
    display: flex;
    align-items: center;
    height: 26.5px;
    font-size: 22px;
    color: var(--ink);
  }
  .contact-list svg {
    width: 20px; height: 20px;
    margin-right: 8px;
    flex: none;
  }

  .card--back .brand-ring {
    left: 248px; top: 104px;
    width: 184px; height: 184px;
    border: 13px solid var(--on-teal);
    display: flex;
    align-items: center;
    justify-content: center;
  }
  .back-wordmark {
    font-weight: 700;
    font-size: 19px;
    color: var(--on-teal);
    white-space: nowrap;
  }
  .back-url {
    position: absolute;
    left: 0; right: 0; top: 342px;
    text-align: center;
    font-size: 21px;
    letter-spacing: 0.6px;
    color: var(--on-teal);
  }
</style>
</head>
<body>
<main class="canvas">
  <section class="card card--front">
    <div class="brand-ring"></div>
    <div class="wordmark">TOM BREVARDI</div>
    <div class="divider"></div>
    <div class="identity">
      <p class="identity__name">Tom Brevardi</p>
      <p class="identity__title">Web Developer</p>
    </div>
    <ul class="contact-list">
      <li>
        <svg viewBox="0 0 20 20" aria-hidden="true"><path fill="#46b79a" d="M2 7c0-3 3-4 8-4s8 1 8 4v1h-4V6.5H6V8H2zM5 9h10l2 7H3z"/></svg>
        570-614-9083
      </li>
      <li>
        <svg viewBox="0 0 20 20" aria-hidden="true"><rect x="1.5" y="4" width="17" height="12" fill="none" stroke="#46b79a" stroke-width="1.6"/><path d="M1.5 4l8.5 7 8.5-7M1.5 16l6-6M18.5 16l-6-6" fill="none" stroke="#46b79a" stroke-width="1.4"/></svg>
        tombrevardi@mailwisp.com
      </li>
      <li>
        <svg viewBox="0 0 20 20" aria-hidden="true"><g fill="none" stroke="#46b79a" stroke-width="1.3"><circle cx="10" cy="10" r="8.5"/><ellipse cx="10" cy="10" rx="3.8" ry="8.5"/><path d="M1.5 10h17M3 5.5h14M3 14.5h14M10 1.5v17"/></g></svg>
        www.tombrevardi.com
      </li>
    </ul>
  </section>

  <section class="card card--back">
    <div class="brand-ring"><span class="back-wordmark">TOM BREVARDI</span></div>
    <div class="back-url">www.tombrevardi.com</div>
  </section>
</main>
</body>
</html>
```